PSD website for property company

Please read the brief thoroughly.

We are looking for a new website for a property group that does property acquisitions, property development and property management.
They buy, build and lease core inner city industrial assets in Sydney, Australia.
They also invest in residential developments.

Site menu
- Home page
- Property – sub menus include – Leasing ; Projects ; Investments ; Property Management
- Capital and finance
- About
- Contact

They like this website
https://www.verlo.com.au/

They want the site to be clean, modern and bold.
They like few colors, even black and white is OK to submit

They have a logo and style guide and useable images here:
http://www.kumet.net/temp/PelorisWeb2019.zip
The zip file is also attached to this project.
We have supplied some images to give you an idea, but we will also require you to provide at least 3 extra images from stock photos.
Use your imagination.

I am expecting a lot of similar designs, so be aware the photos you choose will be really important.
They want really 3 good stock photos used and supplied without charge.
Please not too generic, I repeat the quality of the photos is important.
You may provide several photos (but not in multiple submissions please) and we will choose the best three to be provided.

The winner will be selected on a single home page design and required to provide;
All photos use in original format without charge
A second ‘standard page’ template design based on the winning home page design

```html
<!DOCTYPE html>
<html lang="en">
<head>
<meta charset="utf-8">
<title>Peloris — Property Group</title>
<link href="https://fonts.googleapis.com/css2?family=Montserrat:wght@400;500;600;700&family=Open+Sans:wght@400;600&display=swap" rel="stylesheet">
<style>
:root{
  --green:#6b9a3f;
  --green-dark:#557d2f;
  --ink:#2a2a2a;
  --muted:#6e6e6e;
  --pale:#eef4e4;
  --dark:#2d2f31;
  --darker:#232527;
  --white:#ffffff;
  --line:#e3e3e3;
}
*{box-sizing:border-box;margin:0;padding:0}
html,body{width:1200px;height:3372px;overflow:hidden}
body{position:relative;background:var(--white);font-family:"Open Sans",Arial,sans-serif;color:var(--ink)}
.abs{position:absolute}

/* hero */
.hero{left:0;top:0;width:1200px;height:730px;background:linear-gradient(180deg,#8d95a0 0%,#6f6a64 45%,#4f4b45 80%,#3c3a36 100%)}
.hero-shade{left:0;top:0;width:1200px;height:730px;background:linear-gradient(180deg,rgba(0,0,0,.25),rgba(0,0,0,.05) 40%,rgba(0,0,0,.35))}
.logo{font-family:"Montserrat",Arial,sans-serif;font-weight:600;letter-spacing:8px;font-size:30px;color:var(--white)}
.nav{top:38px;left:420px;display:flex;gap:48px;align-items:center;font-family:"Montserrat",Arial,sans-serif;font-size:13px;color:var(--white)}
.nav .active{padding-bottom:6px;border-bottom:2px solid var(--white)}
.btn-outline{border:1.5px solid var(--white);border-radius:20px;padding:7px 22px;color:var(--white);font-size:13px}
.hero-frame{left:160px;top:150px;width:840px;height:310px;border:3px solid rgba(255,255,255,.85)}
.hero-title{left:0;top:250px;width:1200px;text-align:center;font-family:"Montserrat",Arial,sans-serif;font-weight:700;font-size:54px;line-height:64px;letter-spacing:2px;color:var(--white)}
.btn-green{background:var(--green);color:var(--white);font-family:"Montserrat",Arial,sans-serif;font-size:13px;padding:12px 26px;border-radius:2px}
.hero-btn{left:520px;top:425px}
.dots{left:550px;top:670px;display:flex;gap:14px}
.dots span{width:10px;height:10px;border-radius:50%;background:rgba(255,255,255,.5)}
.dots span.on{background:var(--white)}

/* intro */
.brand-mark{left:0;top:810px;width:1200px;text-align:center;font-family:"Montserrat",Arial,sans-serif;font-weight:600;font-size:30px;letter-spacing:8px;color:var(--green)}
.intro{left:220px;top:860px;width:760px;text-align:center;font-size:23px;line-height:32px;color:var(--ink)}

/* cards */
.card-img{background:linear-gradient(160deg,#c9d3dc,#9a9a92 60%,#7e7a70)}
.card-box{background:var(--white);padding:26px 26px 0 26px;box-shadow:0 2px 10px rgba(0,0,0,.06);border-right:3px solid var(--green)}
.card-box h3{font-family:"Montserrat",Arial,sans-serif;font-weight:600;font-size:20px;margin-bottom:18px;color:var(--ink)}
.card-box p{font-size:13px;line-height:20px;color:var(--muted)}
.more{display:inline-block;margin-top:22px;font-size:13px;color:var(--muted)}
.more.hl{color:var(--ink);border-bottom:2px solid var(--green)}

/* about */
.about-box{left:80px;top:1940px;width:535px;height:430px;background:var(--pale);padding:70px 62px}
.about-box h2{font-family:"Montserrat",Arial,sans-serif;font-weight:600;font-size:38px;margin-bottom:22px}
.about-box p{font-size:13px;line-height:20px;color:var(--muted);margin-bottom:14px}
.btn-line{display:inline-block;margin-top:12px;border:1.5px solid var(--green);border-radius:20px;padding:8px 26px;font-size:13px;color:var(--ink)}
.about-img{left:615px;top:1895px;width:505px;height:525px;background:linear-gradient(150deg,#efe6d6,#cdbb9d 55%,#9b8a6c)}

/* enquire */
.enquire{left:0;top:2480px;width:1200px;height:520px;background:linear-gradient(180deg,#55585a,#3d4042)}
.enquire-shade{left:0;top:2480px;width:1200px;height:520px;background:rgba(30,32,34,.55)}
.enq-title{left:0;top:2540px;width:1200px;text-align:center;font-family:"Montserrat",Arial,sans-serif;font-weight:600;font-size:34px;color:var(--white)}
.enq-sub{left:0;top:2590px;width:1200px;text-align:center;font-size:20px;color:#e8e8e8}
.field{border-bottom:1px solid rgba(255,255,255,.7);color:#e0e0e0;font-size:13px;padding:0 0 10px 8px}
.btn-send{left:520px;top:2890px;border:1.5px solid var(--white);border-radius:20px;padding:9px 30px;color:var(--white);font-size:13px}

/* footer */
.footer{left:0;top:3000px;width:1200px;height:372px;background:var(--dark)}
.contact-label{left:0;top:3070px;width:1200px;text-align:center;font-family:"Montserrat",Arial,sans-serif;font-size:16px;letter-spacing:3px;color:var(--green)}
.phone{left:0;top:3100px;width:1200px;text-align:center;font-size:52px;font-weight:400;color:#b9bcbe}
.email{left:0;top:3175px;width:1200px;text-align:center;font-size:15px;color:#b9bcbe}
.socials{left:545px;top:3240px;display:flex;gap:16px}
.socials span{width:32px;height:32px;border-radius:50%;border:1.5px solid #9ea2a4}
.socials span.on{background:var(--green);border-color:var(--green)}
.bottom-bar{left:0;top:3290px;width:1200px;height:82px;background:var(--darker)}
.copy{left:390px;top:3322px;font-size:13px;color:#9ea2a4}
.copy b{color:var(--white);font-weight:600}
.to-top{left:1075px;top:3310px;width:38px;height:38px;border-radius:50%;background:var(--green);display:flex;align-items:center;justify-content:center}
</style>
</head>
<body>

<!-- Hero -->
<div class="abs hero" role="img" aria-label="Modern brick mid-rise building on a city street corner with trees"></div>
<div class="abs hero-shade"></div>
<div class="abs logo" style="left:80px;top:30px">PELORIS</div>
<nav class="abs nav">
  <span class="active">Home</span><span>Projects</span><span>Capital and Finance</span><span>About Us</span><span>Contact Us</span>
  <span class="btn-outline">Enquire Now</span>
</nav>
<div class="abs hero-frame"></div>
<h1 class="abs hero-title">LOREM IPSUM<br>SIMPLY DUMMY TEXT</h1>
<div class="abs btn-green hero-btn">Explore Our Projects</div>
<div class="abs dots"><span></span><span class="on"></span><span></span><span></span></div>

<!-- Intro -->
<div class="abs brand-mark">PELORIS</div>
<p class="abs intro">There are many variations of passages of lorem Ipsum available, but the majority have suffered alteration in some form, by injected humour, randomised words.</p>

<!-- Row 1 -->
<div class="abs card-img" style="left:80px;top:990px;width:325px;height:245px" role="img" aria-label="Bright open-plan leasing office interior"></div>
<div class="abs card-box" style="left:80px;top:1205px;width:300px;height:190px">
  <h3>Leasing</h3>
  <p>Lorem Ipsum is simply dummy text of the printing and typesetting industry. Lorem Ipsum has been the industry's standard...</p>
  <span class="more">Discover More</span>
</div>

<div class="abs card-img" style="left:437px;top:990px;width:325px;height:245px;background:linear-gradient(160deg,#cfe0ee,#a9b9c6 55%,#7f8d96)" role="img" aria-label="Glass office building against a blue sky"></div>
<div class="abs card-box" style="left:437px;top:1205px;width:300px;height:190px">
  <h3>Investments</h3>
  <p>Lorem Ipsum is simply dummy text of the printing and typesetting industry. Lorem Ipsum has been the industry's standard...</p>
  <span class="more hl">Discover More</span>
</div>

<div class="abs card-img" style="left:795px;top:990px;width:325px;height:245px;background:linear-gradient(160deg,#dfe3e6,#b9aa95 55%,#8c7a62)" role="img" aria-label="Row of arched-window townhouses"></div>
<div class="abs card-box" style="left:795px;top:1205px;width:300px;height:190px">
  <h3>Property Management</h3>
  <p>Lorem Ipsum is simply dummy text of the printing and typesetting industry. Lorem Ipsum has been the industry's standard...</p>
  <span class="more">Discover More</span>
</div>

<!-- Row 2 -->
<div class="abs card-img" style="left:80px;top:1425px;width:505px;height:230px;background:linear-gradient(160deg,#c8d6e2,#8c7c6e 55%,#5e544b)" role="img" aria-label="Brick apartment building on a street corner"></div>
<div class="abs card-box" style="left:80px;top:1615px;width:480px;height:185px">
  <h3>Capital and Finance</h3>
  <p>Lorem Ipsum is simply dummy text of the printing and typesetting industry. Lorem Ipsum has been the industry's standard dummy text ever since the 1500s, when an unknown...</p>
  <span class="more">Explore More</span>
</div>

<div class="abs card-img" style="left:615px;top:1425px;width:505px;height:230px;background:linear-gradient(160deg,#d7e2ea,#c4b59c 55%,#8f8a6a)" role="img" aria-label="Residential development with arched facade and trees"></div>
<div class="abs card-box" style="left:615px;top:1615px;width:480px;height:185px">
  <h3>Our Projects</h3>
  <p>Lorem Ipsum is simply dummy text of the printing and typesetting industry. Lorem Ipsum has been the industry's standard dummy text ever since the 1500s, when an unknown...</p>
  <span class="more">Explore More</span>
</div>

<!-- About -->
<div class="abs about-img" role="img" aria-label="Bright lobby interior with marble floor, sofa and plants"></div>
<div class="abs about-box">
  <h2>About Us</h2>
  <p>There are many variations of passages of Lorem Ipsum available, but the majority have suffered alteration in some form, by injected humour, or randomised words which don't look even slightly plain. If you are going to use a passage.</p>
  <p>you need to be sure there isn't anything embarrassing hidden in the middle of text. All the Lorem Ipsum generators on the Internet tend to repeat predefined chunks.</p>
  <span class="btn-line">Discover More</span>
</div>

<!-- Enquire -->
<div class="abs enquire" role="img" aria-label="Dim street view of a modern building in the background"></div>
<div class="abs enquire-shade"></div>
<h2 class="abs enq-title">Enquire Now</h2>
<p class="abs enq-sub">Contrary to popular belief, Lorem Ipsum is not simply random</p>
<div class="abs field" style="left:210px;top:2668px;width:385px">Name</div>
<div class="abs field" style="left:615px;top:2668px;width:380px">Phone</div>
<div class="abs field" style="left:210px;top:2725px;width:385px">Email</div>
<div class="abs field" style="left:615px;top:2725px;width:380px">Title (message)</div>
<div class="abs field" style="left:210px;top:2782px;width:785px;height:78px">Message</div>
<div class="abs btn-send">Send Message</div>

<!-- Footer -->
<div class="abs footer"></div>
<div class="abs contact-label">CONTACT US</div>
<div class="abs phone">P. 123-456-7890</div>
<div class="abs email">Email: info@peloris.com</div>
<div class="abs socials"><span></span><span class="on"></span><span></span></div>
<div class="abs bottom-bar"></div>
<div class="abs logo" style="left:80px;top:3316px;font-size:22px;letter-spacing:6px">PELORIS</div>
<div class="abs copy">© 2019 <b>Peloris</b>. All Rights Reserved | Terms of Use &amp; Privacy Policy</div>
<div class="abs to-top">
  <svg width="14" height="14" viewBox="0 0 14 14" aria-hidden="true"><path d="M7 12V2M2.5 6.5L7 2l4.5 4.5" stroke="#fff" stroke-width="2" fill="none" stroke-linecap="round" stroke-linejoin="round"/></svg>
</div>

</body>
</html>
```